Small local and internet boutique and custom sewing business that specializes in Custom cothing need

I work in the pagent industry making custom clothing rodeo and show clothing along with refinishing items like furniture and sell and customize items putting the customers own flare on them. I would like that put nicely across from to my customer I want my cards classy and fun shiney and cute. I live on a large ranch and have a cute studio in town were I am starting a boutique

Target Market(s)

women, horse show crowd pageant moms, rodeo queen moms and contestants, boutique shoppers, antique shoppers, ranchers

Requirements
Must have
• Carina@Thegildedpinloft.example
• Phone 575 318 4427
• Instagram Thegildedpinloft
• Facebook www.facebook.com/Thegildedpinloft.example
• Carina Dobbs (Walcott)
• Designer
• Fashion Forward Custom Clothing & Restyled Items

```html
<!DOCTYPE html>
<html lang="en">
<head>
<meta charset="utf-8">
<title>Carina Dobbs – Business Card</title>
<link rel="stylesheet" href="https://fonts.googleapis.com/css2?family=Yellowtail&family=Ubuntu:wght@400;500&display=swap">
<style>
  :root {
    --page: #e8e5e1;
    --card: #232b33;
    --pink: #e39bb2;
    --gold: #e8cb74;
    --brand-gold: #c79d55;
    --green: #3faa3c;
    --white: #ffffff;
  }
  html, body {
    margin: 0;
    width: 1200px;
    height: 900px;
    overflow: hidden;
    background: var(--page);
  }
  .business-card {
    display: block;
    width: 1200px;
    height: 900px;
  }
  .card-face { fill: var(--card); }
  .band-line { fill: var(--pink); }
  .band-gold { fill: var(--gold); }
  .band-ornament { fill: #d9b95f; }
  .emblem-ring { fill: var(--card); }
  .emblem-disc { fill: var(--white); }
  .brand-dot { fill: var(--pink); }
  .tagline {
    font-family: "Ubuntu", sans-serif;
    font-size: 19px;
    fill: var(--pink);
    letter-spacing: 0.3px;
  }
  .brand-name {
    font-family: "Ubuntu", sans-serif;
    font-weight: 500;
    font-size: 32px;
    fill: var(--brand-gold);
  }
  .person-name {
    font-family: "Yellowtail", cursive;
    font-size: 56px;
    fill: var(--green);
  }
  .maiden-name {
    font-family: "Ubuntu", sans-serif;
    font-size: 13px;
    fill: var(--gold);
  }
  .role {
    font-family: "Ubuntu", sans-serif;
    font-size: 24px;
    fill: var(--gold);
  }
  .contact-text {
    font-family: "Ubuntu", sans-serif;
    font-size: 25px;
    fill: var(--pink);
  }
  .contact-badge { fill: var(--pink); }
  .contact-glyph { fill: var(--card); }
  .contact-glyph-line { fill: none; stroke: var(--card); stroke-width: 1.8; }
</style>
</head>
<body>
<svg class="business-card" viewBox="0 0 1200 900" xmlns="http://www.w3.org/2000/svg">
  <rect class="card-face" x="70" y="125" width="1058" height="645" rx="46"/>

  <!-- decorative bands -->
  <g class="band band-left">
    <rect class="band-line" x="68" y="407" width="372" height="8"/>
    <rect class="band-gold" x="68" y="423" width="372" height="51"/>
    <rect class="band-ornament" x="95" y="433" width="320" height="31" rx="15" role="img" aria-label="Dark flourish scroll ornaments"/>
    <rect class="band-line" x="68" y="481" width="372" height="8"/>
  </g>
  <g class="band band-right">
    <rect class="band-line" x="762" y="407" width="366" height="8"/>
    <rect class="band-gold" x="762" y="423" width="366" height="51"/>
    <rect class="band-ornament" x="805" y="433" width="310" height="31" rx="15" role="img" aria-label="Dark flourish scroll ornaments"/>
    <rect class="band-line" x="762" y="481" width="366" height="8"/>
  </g>

  <!-- central emblem -->
  <circle class="emblem-ring" cx="600" cy="432" r="172"/>
  <circle class="emblem-disc" cx="600" cy="432" r="155"/>
  <path id="tagline-arc" d="M 425 432 A 175 175 0 0 1 775 432" fill="none"/>
  <text class="tagline"><textPath href="#tagline-arc" startOffset="50%" text-anchor="middle">Fashion Forward Custom Clothing &amp; Restyled Items</textPath></text>

  <circle class="brand-dot" cx="600" cy="410" r="26"/>
  <text class="brand-name" x="600" y="488" text-anchor="middle">Gilded Pin Loft</text>

  <!-- name block -->
  <text class="person-name" x="1076" y="196" text-anchor="end">Carina Dobbs</text>
  <text class="maiden-name" x="1012" y="215">(Walcott)</text>
  <text class="role" x="868" y="231">Designer</text>

  <!-- contacts -->
  <g class="contact contact-phone">
    <rect class="contact-badge" x="125" y="558" width="32" height="32" rx="5"/>
    <path class="contact-glyph" d="M133 564 l5 -1 l3 7 l-3 2 q2 5 7 8 l2 -3 l7 3 l-1 5 q-1 2 -4 1 q-12 -4 -17 -17 q-1 -3 1 -5 z"/>
    <text class="contact-text" x="186" y="583">575 318 4427</text>
  </g>
  <g class="contact contact-email">
    <rect class="contact-badge" x="125" y="606" width="32" height="32" rx="5"/>
    <rect class="contact-glyph-line" x="131" y="614" width="20" height="15"/>
    <path class="contact-glyph-line" d="M131 614 l10 8 l10 -8 M131 629 l7 -7 M151 629 l-7 -7"/>
    <text class="contact-text" x="186" y="629">Carina@Thegildedpinloft.example</text>
  </g>
  <g class="contact contact-instagram">
    <rect class="contact-badge" x="125" y="651" width="32" height="32" rx="5"/>
    <text class="contact-text" x="186" y="674">Thegildedpinloft</text>
  </g>
  <g class="contact contact-facebook">
    <rect class="contact-badge" x="125" y="697" width="32" height="32" rx="5"/>
    <text class="contact-text" x="181" y="719">www.facebook.com/Thegildedpinloft.example</text>
  </g>
</svg>
</body>
</html>
```